We need a website design for an HVAC (Heating & Air Conditioning) Contractor*

Our HVAC client would like to have a more professional looking site as their current one (https://brindlecoolingworks.example/) is a template site. We will be building the site in-house from the concept.
Items we'd like to incorporate:
- A banner on the homepage that has a click to call plus a form on the right side of the banner
- There is a video on the current website homepage, please find a place to incorporate this.
- We will need to have at least 800 words of content on the homepage, please find space for that (can be a description of a few of the heating / air conditioning services they do). Feel free to use filler content (lorem ipsum) if need be to just show how the content would look

All submissions must have a homepage and a related subpage concept.

```html
<!DOCTYPE html>
<html lang="en">
<head>
<meta charset="utf-8">
<title>Brindle Cooling Works – Heating &amp; Air Conditioning</title>
<link href="https://fonts.googleapis.com/css2?family=Oswald:wght@400;500;600&family=Poppins:wght@300;400;500&display=swap" rel="stylesheet">
<style>
:root{
  --red:#c8281e;
  --navy:#1d3a6a;
  --navy-deep:#18325c;
  --ink:#222;
  --muted:#666;
  --line:#d9d9d9;
  --white:#fff;
}
*{box-sizing:border-box;margin:0;padding:0}
html,body{width:1200px;height:4471px;overflow:hidden}
body{position:relative;font-family:'Poppins',sans-serif;color:var(--ink);background:var(--white)}
.abs{position:absolute}
.brand{font-family:'Oswald',sans-serif;font-weight:600;color:var(--red);font-size:30px;letter-spacing:.5px;display:flex;align-items:center;gap:8px}
.brand .dot{width:14px;height:14px;background:var(--red)}

/* header */
.site-header{left:0;top:0;width:1200px;height:75px;background:#fff;border-bottom:1px solid #eee}
.site-header .brand{position:absolute;left:60px;top:18px}
.nav{position:absolute;left:530px;top:30px;display:flex;gap:20px;font-size:11.5px;color:#333;white-space:nowrap}
.nav .active{color:var(--red);position:relative}
.nav .active:after{content:"";position:absolute;left:50%;top:20px;margin-left:-5px;border:5px solid transparent;border-top-color:var(--red)}
.search{position:absolute;left:914px;top:28px;width:18px;height:18px}
.help{position:absolute;left:955px;top:18px;display:flex;gap:10px;align-items:center}
.help small{display:block;font-size:11px;color:var(--red)}
.help strong{font-family:'Oswald',sans-serif;font-weight:500;color:var(--navy);font-size:16px}

/* hero */
.hero{left:0;top:75px;width:1200px;height:639px;background:linear-gradient(110deg,#6c7178 0%,#8e9298 35%,#4d5560 60%,#2c3440 100%);overflow:hidden}
.hero-red{left:0;top:0;width:1200px;height:639px}
.hero h1{position:absolute;left:60px;top:185px;font-family:'Oswald',sans-serif;font-weight:600;font-size:74px;line-height:80px;color:#fff}
.hero h1 span{color:var(--red)}
.hero p{position:absolute;left:61px;top:363px;color:#fff;font-size:16px;letter-spacing:.3px}
.btn{display:inline-flex;align-items:center;font-family:'Oswald',sans-serif;font-size:17px;color:#fff;background:var(--red);height:38px;padding:0 18px;position:relative}
.btn:after{content:"";position:absolute;right:-20px;top:0;width:10px;height:38px;background:var(--navy);transform:skewX(-25deg)}
.btn.navy{background:var(--navy)}
.btn.navy:after{background:var(--red)}
.hero .btn{position:absolute;left:61px;top:400px}
.slider-ctrl{position:absolute;left:60px;top:578px;display:flex;align-items:center;gap:8px}
.slider-ctrl .c{width:38px;height:38px;border-radius:50%;display:flex;align-items:center;justify-content:center}
.slider-ctrl .c1{background:var(--navy)}
.slider-ctrl .c2{border:2px solid #fff;width:44px;height:44px}
.slider-ctrl .bar{width:84px;height:2px;background:#fff;margin-left:6px}

.form-card{left:795px;top:156px;width:345px;height:511px;background:#fff}
.form-card .corner{position:absolute;left:0;top:0}
.form-card h3{position:absolute;left:0;width:345px;text-align:center;font-family:'Oswald',sans-serif;font-weight:400;line-height:1.2}
.form-card .t1{top:34px;font-size:24px;color:var(--red);padding-left:40px}
.form-card .t2{top:68px;font-size:31px;color:var(--navy);font-weight:500;padding-left:40px}
.field{position:absolute;left:24px;width:300px;height:33px;border:1px solid var(--line);border-radius:3px;font-size:10px;color:#555;padding:9px 12px}
.field.area{height:72px}
.field svg{position:absolute;right:10px;top:10px}
.form-card .btn{position:absolute;left:110px;top:428px;font-size:16px}

/* section titles */
.sec-title{position:absolute;left:0;width:1200px;text-align:center;font-family:'Oswald',sans-serif;font-size:36px;line-height:44px;font-weight:400;color:var(--navy)}
.sec-title span{color:var(--red)}
.sec-sub{position:absolute;left:0;width:1200px;text-align:center;font-size:13px;line-height:18px;color:var(--navy)}
.sec-rule{position:absolute;left:585px;width:30px;height:2px;background:var(--red)}
.photo{position:absolute}
.plus{position:absolute;font-size:22px;color:#999;font-weight:300}

.welcome-text{left:622px;top:902px;width:405px;font-size:11.5px;line-height:19px;color:#333}
.welcome-text p+p{margin-top:12px;color:#555}
.arrow-list{left:622px;top:1082px;font-family:'Oswald',sans-serif;font-size:15px;color:var(--navy)}
.arrow-list li{list-style:none;display:flex;align-items:center;gap:14px;height:38px}

.comfort-band{left:0;top:1181px;width:1200px;height:278px;background:linear-gradient(90deg,#fff 0%,#f3f4f6 50%,#e6e8eb 100%)}
.comfort-small{left:0;top:1255px;width:1200px;text-align:center;font-size:13px;color:var(--red)}
.comfort-head{left:0;top:1281px;width:1200px;text-align:center;font-family:'Oswald',sans-serif;font-size:24px;color:var(--navy)}
.comfort-call{left:398px;top:1339px;display:flex;align-items:center;gap:16px;font-family:'Oswald',sans-serif;color:var(--navy);font-size:17px}
.comfort-call b{color:var(--red);font-weight:500;font-size:24px}

/* services */
.services{left:0;top:1494px;width:637px;height:427px;background:var(--navy)}
.services h2{position:absolute;left:182px;top:66px;font-family:'Oswald',sans-serif;font-weight:400;font-size:36px;line-height:44px;color:#fff}
.services h2 span{color:var(--red)}
.svc{position:absolute;left:180px;display:flex;gap:22px;color:#fff}
.svc .ic{width:68px;height:68px;display:flex;align-items:center;justify-content:center}
.svc h4{font-family:'Oswald',sans-serif;font-weight:400;font-size:22px;margin-bottom:6px}
.svc p{font-size:11px;line-height:20px;color:#d5dcea;width:280px}

/* why */
.why-list{left:608px;top:2130px}
.why-item{display:flex;gap:24px;height:79px}
.why-item .ic{width:52px;height:52px}
.why-item h4{font-family:'Oswald',sans-serif;font-weight:400;font-size:19px;color:var(--navy);margin-top:6px}
.why-item p{font-size:11px;color:#666;margin-top:6px}

/* video */
.video-sec{left:0;top:2541px;width:1200px;height:634px;background:linear-gradient(90deg,#1f3f70,#2b4c7e 50%,#1e3c6c)}
.video-sec .sec-title{color:#fff;top:70px}
.video-sec .sec-sub{color:#fff;top:120px}
.video-frame{left:262px;top:193px;width:676px;height:366px;border:3px solid #111;background:linear-gradient(160deg,#5b5147,#7d8a6f 45%,#b7b8b4 70%,#6a5b4b)}
.video-bar{position:absolute;left:0;bottom:0;width:100%;height:20px;background:#111}
.video-bar .track{position:absolute;left:32px;top:9px;width:560px;height:2px;background:#666}
.play{position:absolute;left:307px;top:150px;width:56px;height:56px}

/* cta */
.cta{left:0;top:3175px;width:1200px;height:264px}
.cta h2{position:absolute;left:0;width:1200px;text-align:center;font-family:'Oswald',sans-serif;font-weight:400;font-size:30px;line-height:42px;color:#fff;top:70px}
.cta .btn{position:absolute;left:527px;top:172px}

/* testimonials */
.card{position:absolute;top:3627px;width:285px;height:368px;background:#fff;box-shadow:0 2px 14px rgba(0,0,0,.1);overflow:hidden}
.card .quote{position:absolute;left:24px;top:34px}
.card p{position:absolute;left:24px;top:98px;width:240px;font-size:11px;line-height:20px;color:#555}
.card .base{position:absolute;left:0;bottom:0}
.card .avatar{position:absolute;left:105px;top:200px;width:76px;height:76px;border-radius:50%;border:3px solid #fff;background:linear-gradient(#c9b8a6,#8f7c6a)}
.card .name{position:absolute;left:0;width:285px;top:288px;text-align:center;font-family:'Oswald',sans-serif;color:#fff;font-size:17px}
.card .stars{position:absolute;left:0;width:285px;top:318px;text-align:center;color:#f3a81c;font-size:12px;letter-spacing:2px}

/* footer */
.site-footer{left:0;top:4073px;width:1200px;height:398px;background:var(--navy-deep)}
.site-footer .brand{position:absolute;left:0;width:1200px;top:90px;justify-content:center;font-size:44px}
.foot-info{position:absolute;left:259px;top:181px;width:681px;height:69px;border:1px solid #3d5887;display:flex}
.foot-info div{flex:1;display:flex;align-items:center;gap:12px;padding-left:14px;color:#fff;font-size:12px;border-right:1px solid #3d5887}
.foot-info div:last-child{border:none}
.foot-info small{display:block;font-size:9px;color:#b8c3d8}
.foot-info b{font-family:'Oswald',sans-serif;font-weight:400;font-size:16px}
.social{position:absolute;left:543px;top:282px;display:flex;gap:12px}
.social i{width:34px;height:34px;border-radius:50%;background:var(--red);display:block}
.copy{position:absolute;left:0;width:1200px;top:330px;text-align:center;color:#c5cfe0;font-size:10px}
</style>
</head>
<body>

<header class="abs site-header">
  <div class="brand"><i class="dot"></i>Brindle</div>
  <nav class="nav"><span class="active">Home</span><span>About Us</span><span>Services</span><span>Testimonials</span><span>Contact Us</span></nav>
  <svg class="search" viewBox="0 0 20 20"><circle cx="8" cy="8" r="5.5" fill="none" stroke="#555" stroke-width="1.6"/><line x1="12" y1="12" x2="17" y2="17" stroke="#555" stroke-width="1.6"/></svg>
  <div class="help">
    <svg width="38" height="38" viewBox="0 0 24 24"><path d="M6.6 10.8a15 15 0 0 0 6.6 6.6l2.2-2.2c.3-.3.7-.4 1-.2 1.1.4 2.3.6 3.6.6.6 0 1 .4 1 1V20c0 .6-.4 1-1 1A17 17 0 0 1 3 4c0-.6.4-1 1-1h3.5c.6 0 1 .4 1 1 0 1.3.2 2.5.6 3.6.1.3 0 .7-.2 1z" fill="var(--red)"/></svg>
    <div><small>Need a Help ? Call Us On:</small><strong>+(1) 555 014 2290</strong></div>
  </div>
</header>

<section class="abs hero" role="img" aria-label="Technician servicing a wall-mounted air conditioning unit with a multimeter">
  <svg class="abs hero-red" viewBox="0 0 1200 639" preserveAspectRatio="none"><polygon points="480,639 1200,0 1200,639" fill="var(--red)" opacity=".85"/></svg>
  <h1>TRUST <span>BRINDLE</span><br>EXPERTS</h1>
  <p>THE HEATING / AIR CONDITIONING SERVICES &nbsp;EXPERTS</p>
  <span class="btn">CONTACT US</span>
  <div class="slider-ctrl">
    <span class="c c1"><svg width="14" height="14" viewBox="0 0 14 14"><path d="M9 2 4 7l5 5" stroke="#fff" stroke-width="2" fill="none"/></svg></span>
    <span class="c c2"><svg width="14" height="14" viewBox="0 0 14 14"><path d="M5 2l5 5-5 5" stroke="#fff" stroke-width="2" fill="none"/></svg></span>
    <span class="bar"></span>
  </div>
</section>

<form class="abs form-card">
  <svg class="corner" width="80" height="80" viewBox="0 0 80 80"><polygon points="0,0 70,0 0,70" fill="var(--navy)"/><polygon points="78,0 84,0 6,78 0,78 0,72" fill="var(--red)"/></svg>
  <h3 class="t1">Schedule</h3>
  <h3 class="t2">An Appointment</h3>
  <div class="field" style="top:133px">Your Name *</div>
  <div class="field" style="top:174px">Your Email *</div>
  <div class="field" style="top:215px">Phone</div>
  <div class="field" style="top:256px">Services<svg width="10" height="10" viewBox="0 0 10 10"><path d="M2 3l3 3 3-3" stroke="#333" stroke-width="1.5" fill="none"/></svg></div>
  <div class="field area" style="top:297px">Description of requirements</div>
  <div class="field" style="top:381px">mm/dd/yyyy<svg width="12" height="12" viewBox="0 0 12 12"><rect x="1" y="2" width="10" height="9" fill="none" stroke="var(--red)"/><line x1="1" y1="5" x2="11" y2="5" stroke="var(--red)"/></svg></div>
  <span class="btn">SUBMIT US</span>
</form>

<h2 class="sec-title" style="top:780px"><span>Welcome To</span> Brindle</h2>
<div class="sec-sub" style="top:830px">Heat &amp; Air Conditioning</div>
<div class="sec-rule" style="top:858px"></div>
<div class="photo" style="left:181px;top:905px;width:389px;height:269px;background:linear-gradient(135deg,#f2efe9,#d7d3cc 60%,#a9a6a0)" role="img" aria-label="Woman relaxing on a sofa under a wall air conditioner"></div>
<span class="plus" style="left:186px;top:1146px">+</span>
<div class="abs welcome-text">
  <p>Lorem Ipsum has been the industry's standard dummy text ever since the, when an unknown printer took a galley of type and scrambled it to make a type specimen book.</p>
  <p>It has survived not only five centuries, but also the leap into electro typesetting, remaining essentially unchanged. It was popularised in the 1960s with the release of Letraset sheets containing Lorem Ipsu passages, and more recently with desktop publishing</p>
</div>
<ul class="abs arrow-list">
  <li><svg width="28" height="12" viewBox="0 0 28 12"><path d="M0 6h26M21 1l5 5-5 5" stroke="var(--red)" stroke-width="1.6" fill="none"/></svg>Heating</li>
  <li><svg width="28" height="12" viewBox="0 0 28 12"><path d="M0 6h26M21 1l5 5-5 5" stroke="var(--red)" stroke-width="1.6" fill="none"/></svg>Air Conditioning</li>
</ul>

<div class="abs comfort-band" role="img" aria-label="Faded image of HVAC technicians"></div>
<div class="abs comfort-small">Your Comfort is Our Top Priority !</div>
<div class="abs comfort-head">Our Experienced HVAC Repair Technicians are Available 24/7 !</div>
<div class="abs comfort-call">Need a Help ? Call Us On:
  <svg width="40" height="40" viewBox="0 0 24 24"><path d="M6.6 10.8a15 15 0 0 0 6.6 6.6l2.2-2.2c.3-.3.7-.4 1-.2 1.1.4 2.3.6 3.6.6.6 0 1 .4 1 1V20c0 .6-.4 1-1 1A17 17 0 0 1 3 4c0-.6.4-1 1-1h3.5c.6 0 1 .4 1 1 0 1.3.2 2.5.6 3.6.1.3 0 .7-.2 1z" fill="var(--red)"/></svg>
  <b>+(1) 555 014 2290</b></div>

<div class="photo" style="left:585px;top:1456px;width:615px;height:413px;background:linear-gradient(120deg,#c9cfd6,#e9ecef 50%,#8a9a78);clip-path:polygon(0 0,100% 0,100% 84%,94% 100%,0 100%)" role="img" aria-label="Technician standing beside an outdoor condenser unit"></div>
<section class="abs services">
  <h2><span>Services</span> We Provide</h2>
  <div class="svc" style="top:148px">
    <span class="ic" style="background:var(--red)"><svg width="40" height="32" viewBox="0 0 40 32"><rect x="3" y="4" width="34" height="14" rx="2" fill="none" stroke="#fff" stroke-width="2"/><path d="M10 22v6M20 22v6M30 22v6" stroke="#fff" stroke-width="2"/></svg></span>
    <div><h4>Air Conditioning</h4><p>Lorem Ipsum has been the industry's standard dummy text ever since the, when an unknown.</p></div>
  </div>
  <div class="svc" style="top:276px">
    <span class="ic" style="background:#fff"><svg width="40" height="36" viewBox="0 0 40 36"><path d="M10 4h20M10 12h20M10 20h20M10 28h20M10 4v24M30 4v24" stroke="var(--red)" stroke-width="2" fill="none"/></svg></span>
    <div><h4>Heating</h4><p>Lorem Ipsum has been the industry's standard dummy text ever since the, when an unknown.</p></div>
  </div>
</section>

<h2 class="sec-title" style="top:1989px"><span>Why Choose</span> Us</h2>
<div class="sec-sub" style="top:2038px">Heat &amp; Air Conditioning</div>
<div class="sec-rule" style="top:2066px"></div>
<div class="photo" style="left:203px;top:2124px;width:375px;height:339px;background:linear-gradient(120deg,#e6e3de,#f4f4f2 50%,#3a3f46);clip-path:polygon(0 0,100% 0,100% 100%,10% 100%,0 90%)" role="img" aria-label="Technician installing an air conditioner while a customer watches"></div>
<span class="plus" style="left:208px;top:2434px">+</span>
<div class="abs why-list">
  <div class="why-item"><svg class="ic" viewBox="0 0 52 52"><circle cx="28" cy="26" r="16" fill="none" stroke="var(--navy)" stroke-width="2.5"/><text x="28" y="31" text-anchor="middle" font-family="Oswald" font-size="14" fill="var(--navy)">24</text><path d="M8 14c-4 8 0 20 8 24" stroke="var(--red)" stroke-width="3" fill="none"/></svg><div><h4>24/7 Emergency Available</h4><p>Lorem ipsum has survived not only five centuries.</p></div></div>
  <div class="why-item"><svg class="ic" viewBox="0 0 52 52"><circle cx="24" cy="24" r="13" fill="none" stroke="var(--navy)" stroke-width="3" stroke-dasharray="5 3"/><circle cx="24" cy="24" r="5" fill="none" stroke="var(--navy)" stroke-width="2"/><path d="M30 30l14 14" stroke="var(--red)" stroke-width="4"/></svg><div><h4>Expert and Professional</h4><p>Lorem ipsum has survived not only five centuries.</p></div></div>
  <div class="why-item"><svg class="ic" viewBox="0 0 52 52"><circle cx="26" cy="22" r="14" fill="none" stroke="var(--navy)" stroke-width="2.5"/><path d="M19 22l5 5 9-10" stroke="var(--red)" stroke-width="3" fill="none"/><path d="M18 34l-4 14 12-6 12 6-4-14" stroke="var(--navy)" stroke-width="2" fill="none"/></svg><div><h4>Satisfaction Guarantee</h4><p>Lorem ipsum has survived not only five centuries.</p></div></div>
  <div class="why-item"><svg class="ic" viewBox="0 0 52 52"><rect x="4" y="8" width="36" height="32" fill="none" stroke="var(--navy)" stroke-width="2.5"/><line x1="4" y1="16" x2="40" y2="16" stroke="var(--navy)" stroke-width="2.5"/><circle cx="36" cy="36" r="8" fill="#fff" stroke="var(--red)" stroke-width="2.5"/><path d="M42 42l6 6" stroke="var(--red)" stroke-width="3"/></svg><div><h4>Free Inspection</h4><p>Lorem ipsum has survived not only five centuries.</p></div></div>
</div>

<section class="abs video-sec">
  <h2 class="sec-title"><span>Watch</span> Video</h2>
  <div class="sec-sub">How It Works</div>
  <div class="sec-rule" style="top:148px"></div>
  <div class="abs video-frame" role="img" aria-label="Video still of a technician repairing an outdoor AC condenser">
    <svg class="play" viewBox="0 0 56 56"><circle cx="28" cy="28" r="26" fill="none" stroke="#fff" stroke-width="3"/><polygon points="23,18 38,28 23,38" fill="#fff"/></svg>
    <div class="video-bar"><span class="track"></span></div>
  </div>
</section>

<section class="abs cta">
  <svg class="abs" style="left:0;top:0" width="1200" height="264" viewBox="0 0 1200 264"><polygon points="0,0 1200,0 1200,220 1150,264 50,264 0,220" fill="var(--red)"/></svg>
  <h2>CALL US TODAY FOR A FREE NO OBLIGATION<br>WRITTEN QUOTE ON</h2>
  <span class="btn navy">CONTACT US</span>
</section>

<h2 class="sec-title" style="top:3508px"><span>Happy</span> Customers</h2>
<div class="sec-sub" style="top:3557px">What our Client Say About Us</div>
<div class="sec-rule" style="top:3586px"></div>

<div class="card" style="left:149px">
  <svg class="quote" width="46" height="36" viewBox="0 0 46 36"><path d="M2 34V20C2 8 10 2 18 2v6c-5 1-8 5-8 10h8v16zM26 34V20C26 8 34 2 42 2v6c-5 1-8 5-8 10h8v16z" fill="var(--red)"/></svg>
  <p>It has survived not only five centuries, but also the leap into electronic typesetting, the remaining essentially unchanged. It was these popularised in the with the</p>
  <svg class="base" width="285" height="150" viewBox="0 0 285 150"><polygon points="0,30 285,0 285,150 0,150" fill="var(--navy)"/></svg>
  <div class="avatar" role="img" aria-label="Client portrait"></div>
  <div class="name">Client Name</div><div class="stars">★★★★★</div>
</div>
<div class="card" style="left:457px">
  <svg class="quote" width="46" height="36" viewBox="0 0 46 36"><path d="M2 34V20C2 8 10 2 18 2v6c-5 1-8 5-8 10h8v16zM26 34V20C26 8 34 2 42 2v6c-5 1-8 5-8 10h8v16z" fill="var(--red)"/></svg>
  <p>It has survived not only five centuries, but also the leap into electronic typesetting, the remaining essentially unchanged. It was these popularised in the with the</p>
  <svg class="base" width="285" height="150" viewBox="0 0 285 150"><polygon points="0,30 285,0 285,150 0,150" fill="var(--red)"/></svg>
  <div class="avatar" role="img" aria-label="Client portrait"></div>
  <div class="name">Client Name</div><div class="stars">★★★★★</div>
</div>
<div class="card" style="left:764px">
  <svg class="quote" width="46" height="36" viewBox="0 0 46 36"><path d="M2 34V20C2 8 10 2 18 2v6c-5 1-8 5-8 10h8v16zM26 34V20C26 8 34 2 42 2v6c-5 1-8 5-8 10h8v16z" fill="var(--red)"/></svg>
  <p>It has survived not only five centuries, but also the leap into electronic typesetting, the remaining essentially unchanged. It was these popularised in the with the</p>
  <svg class="base" width="285" height="150" viewBox="0 0 285 150"><polygon points="0,30 285,0 285,150 0,150" fill="var(--navy)"/></svg>
  <div class="avatar" role="img" aria-label="Client portrait"></div>
  <div class="name">Client Name</div><div class="stars">★★★★★</div>
</div>

<footer class="abs site-footer">
  <div class="brand"><i class="dot"></i>Brindle</div>
  <div class="foot-info">
    <div><svg width="20" height="26" viewBox="0 0 20 26"><path d="M10 25S2 15 2 9a8 8 0 0 1 16 0c0 6-8 16-8 16z" fill="none" stroke="var(--red)" stroke-width="2"/><circle cx="10" cy="9" r="3" fill="var(--red)"/></svg><span>Brindle Cooling Works<small>101 - Lorem ipsum simple text.</small></span></div>
    <div><svg width="22" height="22" viewBox="0 0 24 24"><path d="M6.6 10.8a15 15 0 0 0 6.6 6.6l2.2-2.2c.3-.3.7-.4 1-.2 1.1.4 2.3.6 3.6.6.6 0 1 .4 1 1V20c0 .6-.4 1-1 1A17 17 0 0 1 3 4c0-.6.4-1 1-1h3.5c.6 0 1 .4 1 1 0 1.3.2 2.5.6 3.6.1.3 0 .7-.2 1z" fill="var(--red)"/></svg><span><small>Phone :</small><b>+(1) 555 014 2290</b></span></div>
    <div><svg width="24" height="18" viewBox="0 0 24 18"><rect x="1" y="1" width="22" height="16" fill="var(--red)"/><path d="M1 1l11 9 11-9" stroke="#fff" stroke-width="1.6" fill="none"/></svg><span><small>Email :</small>info@brindlecooling.example</span></div>
  </div>
  <div class="social"><i></i><i></i><i></i></div>
  <div class="copy">©Brindle Cooling Works – 2021 All rights reserved.</div>
</footer>

</body>
</html>
```